Varrick Development and Management Corp Stationery Design Project

Based on the logo, a stationary format that can be used for correspondence with all project stakeholders. Typically this involves landowners, public officials, general public, and investors. It needs to be clean and professional, representing the two engineers that manage the company.
Updates

Target Market(s)

Public officials, investors, project stakeholders, and landowners. All or english speaking, residing in North America. Company is based in Calgary, Alberta, Canada. Project values range fro $10MM to $500MM CAD.

Industry/Entity Type

It Company

Requirements
Should not have
• No references to tropics, palm trees, or similar beaches.

```html
<!DOCTYPE html>
<html lang="en">
<head>
<meta charset="utf-8">
<title>Varrick Development and Management Corp – Presentation Folder</title>
<link href="https://fonts.googleapis.com/css2?family=Didact+Gothic&display=swap" rel="stylesheet">
<style>
  :root {
    --page-bg: #d9d9d9;
    --folder: #333336;
    --folder-edge: #2b2b2e;
    --accent: #a6c120;
    --building-grey: #8a8c90;
    --text-grey: #9a9ca0;
  }
  * { margin: 0; padding: 0; box-sizing: border-box; }
  html, body {
    width: 1200px; height: 966px; overflow: hidden;
    background: var(--page-bg);
    font-family: "Didact Gothic", "Century Gothic", sans-serif;
  }
  .folder-spread {
    position: absolute;
    left: 180px; top: 170px;
    width: 840px; height: 600px;
    display: flex;
  }
  .folder-panel {
    position: relative;
    width: 420px; height: 600px;
    background: var(--folder);
    overflow: hidden;
  }
  .folder-panel--back { border-right: 1px solid var(--folder-edge); }
  .accent-band {
    position: absolute; left: 0; right: 0; bottom: 0;
    height: 8px;
    background: var(--accent);
  }
  .skyline-artwork {
    position: absolute;
    bottom: 8px;
    height: 190px;
    background: linear-gradient(to top, var(--accent) 0%, var(--building-grey) 45%, rgba(138,140,144,0.55) 100%);
  }
  .folder-panel--back .skyline-artwork { right: 0; width: 175px; }
  .folder-panel--front .skyline-artwork { left: 0; width: 270px; }
  .brand-block {
    position: absolute;
    top: 60px; right: 40px;
    text-align: left;
  }
  .brand-name {
    display: flex; align-items: center; gap: 8px;
    color: var(--accent);
    font-size: 26px;
    letter-spacing: 1px;
    line-height: 1;
  }
  .brand-mark {
    width: 14px; height: 14px;
    background: var(--accent);
  }
  .brand-tagline {
    margin-top: 4px;
    margin-left: 22px;
    color: var(--text-grey);
    font-size: 9px;
  }
  .contact-lines {
    position: absolute;
    z-index: 1;
    left: 22px; bottom: 20px;
    width: 215px;
    color: var(--text-grey);
    font-size: 7.5px;
    font-style: normal;
    line-height: 1.45;
    white-space: nowrap;
  }
  .contact-label { color: var(--accent); }
</style>
</head>
<body>
  <main class="folder-spread">
    <section class="folder-panel folder-panel--back">
      <div class="skyline-artwork" role="img" aria-label="Stylised city skyline illustration of grey buildings with green peaks, continuing across the spine"></div>
      <address class="contact-lines">
        Harbour Point Head Office · P.O.Box 40517 Calgary, AB<br>
        <span class="contact-label">Tel:</span> +1 403 555 0148 · <span class="contact-label">E-mail:</span> info@varrick.com · www.varrick.com
      </address>
      <div class="accent-band"></div>
    </section>
    <section class="folder-panel folder-panel--front">
      <div class="brand-block">
        <div class="brand-name"><span class="brand-mark"></span>VARRICK</div>
        <div class="brand-tagline">Development and Management Corp</div>
      </div>
      <div class="skyline-artwork" role="img" aria-label="Stylised city skyline illustration of grey buildings with green peaks, continued from the back cover"></div>
      <div class="accent-band"></div>
    </section>
  </main>
</body>
</html>
```